Ansprechendes Layout für Geschichte von Oldtimern
Grossartiges Design, supernette Zusammenarbeit, megaschnelle Rückmeldung auf meine dusseligen Fragen - dass "Kastrel Ubo" sich meines Projektes angenommen hat, war ein echter Glückstreffer! Ich bin sowohl mit dem Ergebnis als auch mit der Kommunikation während des gesamten Prozesses absolut happy! Das hat richtig Spaß gemacht und auf meine Oldtimer-"Broschüre" bin ich stolz wie Bolle... Schade, dass man hier nicht 10 Sterne vergeben kann - "Kastrel Ubo" hätte sie verdient!
Zielgruppe
Ich mache mich aktuell selbstständig als Solo-Freiberuflerin (Redakteurin) mit dem Projekt 'Die Lack-Ballade': Ich schreibe für Oldtimer-Besitzer die Lebensgeschichte ihres Oldtimers auf - lebendig und augenzwinkernd. Zielgruppe: Oldtimer-Besitzer, die die Historie ihres Wagens als individuelles 'Buch' haben möchten; für sich selbst oder auch als Verkaufsargument beim Weiterverkauf des Oldtimers.
Aufgabenstellung
Mein Text wird auf hochwertigem Papier (einseitig) gedruckt , im Format A4 quer. Ein paar gut platzierte Fotos sollen den Text 'auflockern'. Für dieses Layout von Titelseite sowie Text & Fotos suche ein 'hinreißendes' Design (Schriften und Layout). Die fertigen Seiten werden dann in einer Druckerei ausgedruckt und in einen A4 Querformat-Klemmbinder 'reingesteckt'. Deswegen muss links entsprechend viel Rand/Platz gelassen werden. Wichtig ist mir eine sehr edle und hochwertige Anmutung des Layouts. Es soll kein 'Bildband' werden, die Fotos ergänzen lediglich den Text, der 'im Mittelpunkt' steht.

```html
<!DOCTYPE html>
<html lang="de">
<head>
<meta charset="utf-8">
<title>Die Lack-Ballade – Seiten</title>
<link rel="stylesheet" href="https://fonts.googleapis.com/css2?family=Fira+Sans:wght@300;400&family=Open+Sans:wght@400&display=swap">
<style>
  :root {
    --gold: #b5a05a;
    --dark: #333333;
    --paper: #ffffff;
    --ink: #1e1e1e;
    --backdrop: #ffffff;
  }
  * { margin: 0; padding: 0; box-sizing: border-box; }
  html, body { width: 1200px; height: 2554px; overflow: hidden; background: var(--backdrop); }
  body { position: relative; font-family: "Open Sans", sans-serif; color: var(--ink); }

  .page { position: absolute; background: var(--paper); box-shadow: 4px 5px 8px rgba(0,0,0,.35); overflow: hidden; }
  .page--cover { left: 48px; top: 60px; width: 1110px; height: 784px; }
  .page--story-1 { left: 45px; top: 884px; width: 1110px; height: 788px; }
  .page--story-2 { left: 50px; top: 1726px; width: 1110px; height: 789px; }

  .cover-photo { position: absolute; left: 0; top: 0; width: 1110px; height: 627px;
    background: linear-gradient(180deg, #2f5a1e 0%, #3d6b27 45%, #1c2535 62%, #28324a 80%, #8d8f8d 100%); }
  .cover-band { position: absolute; left: 0; top: 627px; width: 1110px; height: 157px; background: var(--dark); }
  .cover-title { position: absolute; left: 70px; top: 668px; font-family: "Fira Sans", sans-serif; font-weight: 300;
    font-size: 38px; letter-spacing: 1px; color: #fff; white-space: nowrap; }

  .brand { position: absolute; display: flex; align-items: center; gap: 12px;
    font-family: "Fira Sans", sans-serif; font-weight: 300; color: #fff; white-space: nowrap; line-height: 1; }
  .brand__mark { background: var(--gold); flex: none; }
  .brand--cover { right: 77px; top: 678px; font-size: 36px; }
  .brand--cover .brand__mark { width: 22px; height: 22px; }

  .top-bar { position: absolute; left: 0; top: 0; width: 100%; height: 21px; background: var(--dark); }

  .footer { position: absolute; left: 0; width: 100%; height: 80px; }
  .footer__rule { position: absolute; left: 0; width: 100%; height: 1px; background: var(--dark); }
  .footer__band { position: absolute; left: 0; width: 100%; height: 57px; background: var(--gold); top: 9px; }
  .footer .brand { right: 70px; top: 24px; font-size: 24px; }

  .wide-photo { position: absolute; left: 119px; top: 186px; width: 915px; height: 206px;
    background: linear-gradient(180deg, #466f2d 0%, #3a5f26 35%, #1c2638 55%, #222c40 82%, #8a8c88 100%); }
  .body-text { position: absolute; font-size: 13.6px; line-height: 19.6px; text-align: justify; }
  .page--story-1 .body-text { left: 119px; top: 418px; width: 915px; }

  .gauge-photo { position: absolute; left: 120px; top: 179px; width: 348px; height: 348px; border-radius: 50%;
    border: 4px solid var(--gold); background: radial-gradient(circle at 50% 45%, #6a6a68 0%, #3a3a3a 55%, #1e1e1e 100%); }
  .page--story-2 .body-text { left: 522px; top: 245px; width: 512px; font-size: 13.2px; }
</style>
</head>
<body>

<section class="page page--cover">
  <div class="cover-photo" role="img" aria-label="Foto: dunkelblaue Oldtimer-Limousine mit Weißwandreifen vor grüner Hecke"></div>
  <div class="cover-band"></div>
  <h1 class="cover-title">»Ein Charmeur und Gentleman«</h1>
  <div class="brand brand--cover"><span class="brand__mark"></span>Die Lack-Ballade</div>
</section>

<section class="page page--story-1">
  <div class="top-bar"></div>
  <div class="wide-photo" role="img" aria-label="Foto: Seitenansicht der dunkelblauen Limousine mit Heckflossen"></div>
  <p class="body-text">Eigentlich wollte der Torben mich ja behalten. Eigentlich… Aber dann kam alles ganz anders. Damals. Vor fast 15 Jahren. Da rumpelte nämlich eines Tages der Heiko mit seinem weißen Firmen-Transporter bei uns auf den Hof, schleppte jede Menge Werkzeug und andere Gerätschaften ins Haus, baute tagelang das Bad und die Küche von Torben um – und als er auch mal in die Garage reinguckte, stand er plötzlich vor mir. Ich hab’s ja ehrlich gesagt gleich gesehen: Dieser liebevolle und staunende Blick…! Keine Frage: Der Mann war vom Fleck weg von mir begeistert. Ich hab’ leise geschmunzelt und mich natürlich von meiner schönsten Seite gezeigt: Mein Blau schimmerte edel, der Hochkühler funkelte im Licht, und meine schicke Heckflosse ist an Eleganz sowieso nicht zu überbieten. Kein Wunder, dass es ihn da voll erwischt hat… Die beiden haben dann noch ein bisschen verhandelt, denn der Torben wollte mich ja behalten. Eigentlich. Aber ich ahnte es da schon längst: Demnächst steht bestimmt ein Umzug an!</p>
  <div class="footer" style="top:671px">
    <div class="footer__rule" style="top:0"></div>
    <div class="footer__band"></div>
    <div class="footer__rule" style="top:74px"></div>
    <div class="brand">Die Lack-Ballade</div>
  </div>
</section>

<section class="page page--story-2">
  <div class="top-bar"></div>
  <div class="gauge-photo" role="img" aria-label="Foto: Nahaufnahme des Tachometers mit Tank- und Temperaturanzeige"></div>
  <p class="body-text">„Ich fand den einfach knuffig – und das sind so solide und stabile Modelle. Die liefen einfach.“, hat der Heiko neulich einer Bekannten gestanden, der er unsere gemeinsame Geschichte erzählt hat. „Knuffig“ – von wegen! Verliebt hat er sich in mich! Und zwar Hals über Kopf! Und das ist ja, bei genauerer Betrachtung, auch kein Wunder: Denn als der Heiko noch klein war, da fuhren meine Geschwister ja noch in großer Anzahl durch die Gegend, oft auch als Taxis. Schon damals war der junge Heiko von unserer Valmora-Familie so begeistert, dass er deswegen sogar Taxifahrer werden wollte! Daraus ist dann bekanntlich ja nichts geworden. Denn statt Taxifahrer zu werden, hat er 1993 in fünfter Generation das familiäre Sanitär-Unternehmen übernommen. Und das war auch sehr gut so – womöglich hätten wir uns sonst ja nie kennengelernt!</p>
  <div class="footer" style="top:672px">
    <div class="footer__rule" style="top:0"></div>
    <div class="footer__band"></div>
    <div class="footer__rule" style="top:74px"></div>
    <div class="brand">Die Lack-Ballade</div>
  </div>
</section>

</body>
</html>
```